Billboard design for retail kitchen cabinet business

We have a large 7,000 square-foot showroom of beautiful kitchen cabinet displays of all different designs and price ranges. In business for over 50 years with expert designers.
Full size Norvale Media 14' X 48' billboard
Target Market(s)
Retail public on high traffic Los Angeles streets

```html
<!DOCTYPE html>
<html lang="en">
<head>
<meta charset="utf-8">
<title>Hearthline Cabinets Billboard</title>
<link href="https://fonts.googleapis.com/css2?family=Oswald:wght@500;600;700&display=swap" rel="stylesheet">
<style>
  :root {
    --backdrop: #5f5f64;
    --paper: #ffffff;
    --ink: #1c1c1c;
    --bar: #262626;
    --orange-deep: #f0900f;
    --orange-light: #f9bc35;
    --umber: #5f5540;
    --umber-dark: #4a4231;
    --photo-warm: #b89066;
    --photo-dark: #5a3b26;
    --photo-cream: #e6d3a8;
  }
  * { margin: 0; padding: 0; box-sizing: border-box; }
  html, body {
    width: 963px; height: 1200px; overflow: hidden;
    background: var(--backdrop);
    font-family: "Oswald", "Arial Narrow", sans-serif;
  }
  .billboard-stage {
    position: absolute; left: 31px; top: 469px;
    width: 1020px; height: 297px;
    transform: scale(0.882); transform-origin: 0 0;
  }
  .billboard {
    position: relative; width: 1020px; height: 297px;
    background: var(--paper); overflow: hidden;
  }
  .billboard-art { position: absolute; inset: 0; }
  .headline {
    position: absolute; left: 34px; top: 12px;
    line-height: 1; font-weight: 600; text-transform: uppercase;
  }
  .headline-accent {
    display: block; font-size: 51px; letter-spacing: 0.2px;
    background: linear-gradient(180deg, var(--orange-light), var(--orange-deep));
    -webkit-background-clip: text; background-clip: text; color: transparent;
  }
  .headline-main {
    display: block; margin-top: 6px; font-size: 58px; color: var(--ink);
    letter-spacing: 0.3px;
  }
  .showroom-note {
    position: absolute; left: 34px; top: 150px;
    color: var(--paper); font-size: 19px; font-weight: 500;
    text-transform: uppercase; letter-spacing: 0.1px;
  }
  .contact-line {
    position: absolute; left: 30px; display: flex; align-items: center; gap: 14px;
    color: #2e2e2e; font-weight: 600;
  }
  .contact-phone { top: 198px; font-size: 42px; }
  .contact-web { top: 251px; font-size: 22px; font-weight: 500; }
  .contact-icon { flex: none; }
  .brand-name {
    position: absolute; left: 505px; top: 180px;
    display: flex; align-items: center; gap: 10px;
    color: var(--paper); font-weight: 600; font-size: 26px;
    line-height: 1.05; text-transform: uppercase;
  }
  .brand-square { width: 14px; height: 14px; background: var(--paper); flex: none; }
</style>
</head>
<body>
  <div class="billboard-stage">
    <section class="billboard">
      <svg class="billboard-art" viewBox="0 0 1020 297" width="1020" height="297">
        <defs>
          <linearGradient id="photoWarm" x1="0" y1="0" x2="1" y2="1">
            <stop offset="0" stop-color="#7a6a5c"/>
            <stop offset="0.5" stop-color="var(--photo-warm)"/>
            <stop offset="1" stop-color="var(--photo-dark)"/>
          </linearGradient>
          <linearGradient id="photoCream" x1="0" y1="0" x2="0" y2="1">
            <stop offset="0" stop-color="var(--photo-cream)"/>
            <stop offset="1" stop-color="#8a5e3c"/>
          </linearGradient>
        </defs>
        <polygon role="img" aria-label="Photo of kitchen showroom displays with cabinets and counters"
                 points="530,0 1020,0 1020,297 810,297 590,58" fill="url(#photoWarm)"/>
        <polygon points="1020,70 812,297 832,297 1020,92" fill="var(--paper)"/>
        <polygon points="787,-4 951,140 807,284 653,140" fill="var(--paper)"/>
        <polygon role="img" aria-label="Photo of a cream kitchen with island counter and food"
                 points="787,8 938,140 807,271 666,140" fill="url(#photoCream)"/>
        <polygon points="330,297 578,58 598,58 352,297" fill="var(--umber-dark)"/>
        <polygon points="352,297 598,58 810,297" fill="var(--umber)"/>
        <polygon points="0,137 495,137 440,192 0,192" fill="var(--bar)"/>
      </svg>

      <h1 class="headline">
        <span class="headline-accent">Beautifying Kitchens</span>
        <span class="headline-main">For Over 50 Years</span>
      </h1>

      <p class="showroom-note">We have a large 7,000 square-foot showroom</p>

      <p class="contact-line contact-phone">
        <svg class="contact-icon" width="30" height="30" viewBox="0 0 24 24" aria-hidden="true">
          <path d="M6.6 10.8c1.4 2.8 3.8 5.1 6.6 6.6l2.2-2.2c.3-.3.7-.4 1-.2 1.1.4 2.3.6 3.6.6.6 0 1 .4 1 1V20c0 .6-.4 1-1 1C10.6 21 3 13.4 3 4c0-.6.4-1 1-1h3.5c.6 0 1 .4 1 1 0 1.3.2 2.5.6 3.6.1.3 0 .7-.2 1l-2.3 2.2z" fill="var(--orange-deep)"/>
        </svg>
        (310) 555-0148
      </p>

      <p class="contact-line contact-web">
        <svg class="contact-icon" width="30" height="26" viewBox="0 0 24 24" aria-hidden="true">
          <g fill="none" stroke="var(--orange-deep)" stroke-width="1.8">
            <circle cx="12" cy="12" r="9"/>
            <ellipse cx="12" cy="12" rx="4" ry="9"/>
            <line x1="3" y1="12" x2="21" y2="12"/>
            <line x1="5" y1="7" x2="19" y2="7"/>
            <line x1="5" y1="17" x2="19" y2="17"/>
          </g>
        </svg>
        www.hearthlinecabinets.net
      </p>

      <div class="brand-name">
        <span class="brand-square"></span>
        <span>Hearthline<br>Cabinets</span>
      </div>
    </section>
  </div>
</body>
</html>
```